Keldro Cybersecurity Secives professional web site

Keldro is a unit of the Vostemic company, based on the audit services it offers and which mainly works by the contacts it has from its previous experience. The objective with the development of this website will be to increase its presence on the internet and even link the traffic of its social networks with the blog of the new page and in this way, provide information for old and potential customers.
For this reason, we will set the objective of the page, have all the information of the company, its services and its scope in general, in a formal and simple for users, facilitating the task of finding the information they want within of the page, as well as, including the option of feedback.
Updates

Need extra days to review

Target Market(s)

any company that needs security assessments

Number of Pages Required

4 page

Font styles to use
Sans Serif

Colors

Designer to choose colors to be used in the design.

Requirements
Must have
• READ THE PDF PLEASE. Video in homepage, cool graphics, color like our logo
• I like the following sites: www.vostemic-example.com & www.gantrelo-example.com
Nice to have
• Futuristic
Should not have
• Please, dont use the gallery pictures I used in my document, I prefer hand made illustrations instead

```html
<!DOCTYPE html>
<html lang="en">
<head>
<meta charset="utf-8">
<title>Keldro Security</title>
<link rel="stylesheet" href="https://fonts.googleapis.com/css2?family=Montserrat:wght@700;800&family=Arimo:wght@400;600&display=swap">
<style>
:root{
  --navy:#15202e;
  --navy-deep:#0d1622;
  --red:#b8141f;
  --page:#eef1f6;
  --panel:#e3e7ee;
  --white:#ffffff;
  --text:#4a5260;
  --muted:#8b93a0;
  --grey-ring:#dde0e5;
}
*{margin:0;padding:0;box-sizing:border-box}
html,body{width:1200px;height:2560px;overflow:hidden}
body{position:relative;background:var(--page);font-family:"Arimo",sans-serif;color:var(--text)}
.abs{position:absolute}
.heading{font-family:"Montserrat",sans-serif;font-weight:800;color:var(--navy)}

/* header */
.site-header{left:0;top:0;width:1200px;height:105px;background:var(--page)}
.brand{display:flex;align-items:center;gap:14px}
.brand-name{font-family:"Montserrat",sans-serif;font-weight:800;font-size:31px;line-height:30px;color:var(--navy);letter-spacing:0.5px}
.brand-dot{width:62px;height:62px;border-radius:50%;background:var(--navy)}
.site-header .brand{left:77px;top:20px}
.main-nav{right:40px;top:36px;display:flex;align-items:center;gap:28px;font-family:"Arimo",sans-serif;font-weight:400;font-size:15px;color:var(--navy)}
.main-nav .lang{display:flex;align-items:center;gap:8px;font-size:13.5px}
.flag{width:34px;height:34px;border-radius:50%}
.flag-en{background:#2b3f8f}
.flag-es{background:#d9a21c}
.nav-mark{width:12px;height:12px;border-radius:50%;background:var(--navy);display:inline-block;margin-right:10px;vertical-align:-1px}

/* hero */
.hero{left:0;top:105px;width:1200px;height:620px}
.hero-text{left:77px;top:165px;width:540px;color:var(--white)}
.hero-title{font-family:"Montserrat",sans-serif;font-weight:800;font-size:48px;letter-spacing:0.5px}
.hero-sub{font-size:23px;letter-spacing:1px;margin-top:8px}
.hero-copy{font-size:14.5px;line-height:29px;margin-top:12px;color:#dfe4ec}
.btn{display:flex;align-items:center;justify-content:center;background:var(--red);color:var(--white);font-family:"Montserrat",sans-serif;font-weight:800;font-size:21px;border-radius:28px;letter-spacing:0.5px}
.hero .btn{left:77px;top:378px;width:208px;height:55px}
.slide-arrow{width:44px;height:44px;border-radius:50%;background:rgba(255,255,255,0.08)}

/* services */
.section-title{font-size:44px;text-align:center;width:1200px;left:0}
.section-sub{font-size:19px;color:var(--red);text-align:center;width:1200px;left:0}
.service-card{width:250px;height:325px;top:838px;background:var(--white);text-align:center}
.service-card .thumb{position:absolute;left:17px;top:18px;width:216px;height:126px}
.service-card h3{position:absolute;left:10px;right:10px;top:168px;font-family:"Montserrat",sans-serif;font-weight:800;font-size:16px;line-height:22px;color:var(--navy);letter-spacing:0.5px}
.service-card p{position:absolute;left:20px;right:20px;top:224px;font-size:14px;line-height:25px;color:var(--text)}
.card-bar{position:absolute;left:38px;width:174px;height:4px;background:var(--red)}
.dot{width:14px;height:14px;border-radius:50%}

/* company */
.company-copy{left:77px;top:1380px;width:520px;font-size:14px;line-height:29px}
.company-copy p+p{margin-top:10px}

/* contact */
.contact-panel{left:193px;top:1737px;width:813px;height:415px;background:var(--panel);border-radius:6px}
.field{background:var(--white);border-radius:6px;font-size:13.5px;color:var(--text);padding:12px 14px}

/* footer */
.footer-title{font-family:"Montserrat",sans-serif;font-weight:800;font-size:15px;color:var(--white);letter-spacing:1px}
.footer-list{font-size:14px;line-height:27px;color:#b9c0cb}
.social{width:40px;height:40px;border-radius:50%;border:2px solid #9aa3b0}
.contact-row{display:flex;align-items:flex-start;gap:16px;font-size:14px;line-height:22px;color:#b9c0cb}
</style>
</head>
<body>

<header class="site-header abs">
  <div class="brand abs">
    <div class="brand-name">KELDRO<br>SECURITY</div>
    <div class="brand-dot"></div>
  </div>
  <nav class="main-nav abs">
    <span><i class="nav-mark"></i>THE START</span>
    <span>SERVICES</span>
    <span>BLOG</span>
    <span>CONTACT</span>
    <span class="lang"><i class="flag flag-en"></i>English</span>
    <span class="lang"><i class="flag flag-es"></i>Spanish</span>
  </nav>
</header>

<section class="hero abs">
  <svg class="abs" style="left:0;top:0" width="1200" height="620" viewBox="0 0 1200 620">
    <defs>
      <linearGradient id="heroShade" x1="0" y1="0" x2="1" y2="1">
        <stop offset="0" stop-color="#1a2433"/>
        <stop offset="0.6" stop-color="#2c3746"/>
        <stop offset="1" stop-color="#111a26"/>
      </linearGradient>
    </defs>
    <path role="img" aria-label="Dark photo of a laptop keyboard with a padlock" d="M0 0H1200V515C1060 505 920 510 760 540C560 580 300 640 0 610Z" fill="url(#heroShade)"/>
  </svg>
  <div class="hero-text abs">
    <h1 class="hero-title">KELDRO SECURITY</h1>
    <div class="hero-sub">SOURCE CODE AUDIT</div>
    <p class="hero-copy">Our company is committed to perform services with the aim of improving the quality of security, with the highest ethics and responsibility, treating your data confidentially &amp; integrally</p>
  </div>
  <div class="btn abs">GET STARTED</div>
  <div class="slide-arrow abs" style="left:16px;top:245px"><svg width="44" height="44"><path d="M25 14L17 22L25 30" stroke="#fff" stroke-width="2" fill="none"/></svg></div>
  <div class="slide-arrow abs" style="left:1138px;top:245px"><svg width="44" height="44"><path d="M19 14L27 22L19 30" stroke="#fff" stroke-width="2" fill="none"/></svg></div>
  <svg class="abs" style="left:652px;top:92px" width="466" height="466" viewBox="0 0 466 466">
    <defs>
      <linearGradient id="videoShade" x1="0" y1="0" x2="1" y2="1">
        <stop offset="0" stop-color="#2b4a68"/>
        <stop offset="1" stop-color="#0f1b2a"/>
      </linearGradient>
    </defs>
    <circle cx="233" cy="233" r="233" fill="#fff"/>
    <circle role="img" aria-label="Video still of a person working at screens in a server room" cx="233" cy="233" r="222" fill="url(#videoShade)"/>
    <rect x="198" y="208" width="70" height="52" rx="12" fill="var(--red)"/>
    <path d="M222 220L248 234L222 248Z" fill="#fff"/>
  </svg>
</section>

<h2 class="heading section-title abs" style="top:732px">OUR SERVICE</h2>
<div class="section-sub abs" style="top:786px">What We Do</div>

<article class="service-card abs" style="left:77px">
  <div class="card-bar" style="top:-2px"></div>
  <div class="thumb" role="img" aria-label="Photo of a hand writing on bar chart paper" style="background:linear-gradient(135deg,#ecebe6,#a9825c)"></div>
  <h3>WEBPAGE AUDIT</h3>
  <p>Within this service we offer the vulnerability scan in network, servers &amp; protocol.</p>
  <div class="card-bar" style="bottom:-2px"></div>
</article>
<article class="service-card abs" style="left:342px">
  <div class="thumb" role="img" aria-label="Photo of a data center corridor" style="background:linear-gradient(135deg,#3a3f47,#15181d)"></div>
  <h3>INTERNAL &amp; EXTERNAL AUDIT</h3>
  <p>Within this service we offer the vulnerability scan in network, servers &amp; protocol.</p>
</article>
<article class="service-card abs" style="left:608px">
  <div class="thumb" role="img" aria-label="Photo of a desk with a laptop and documents" style="background:linear-gradient(135deg,#6b5446,#d8cfc7)"></div>
  <h3>WEB APPLICATION AUDIT</h3>
  <p>Within this service we offer the vulnerability scan in network, servers &amp; protocol.</p>
</article>
<article class="service-card abs" style="left:873px">
  <div class="thumb" role="img" aria-label="Photo of a digital padlock on a security screen" style="background:linear-gradient(135deg,#1d2b46,#2c63b7)"></div>
  <h3>SOURCE CODE<br>AUDIT</h3>
  <p>Within this service we offer the vulnerability scan in network, servers &amp; protocol.</p>
</article>
<div class="dot abs" style="left:582px;top:1191px;background:var(--red)"></div>
<div class="dot abs" style="left:603px;top:1191px;background:#fff;border:1px solid #c5c9d0"></div>

<h2 class="heading abs" style="left:77px;top:1282px;font-size:44px">OUR COMPANY</h2>
<div class="abs" style="left:77px;top:1337px;font-size:18px;color:var(--red)">What Is Cybersecurity?</div>
<div class="company-copy abs">
  <p>Cybersecurity is a recent phenomenon, which allows us to be protected from cyber attacks, in a certain way, it is the key to the future for business, since it allows you to protect all the information of it.</p>
  <p>After eight years of experience in the sector, we offer with our services, the reputation and stability of the companies that we audit, minimizing and avoiding the risk of information losses and thus helping the management in their businesses, therefore, making the same , safe and stable companies.</p>
</div>
<div class="btn abs" style="left:77px;top:1612px;width:198px;height:51px">LEARN MORE</div>
<svg class="abs" style="left:590px;top:1255px" width="540" height="420" viewBox="0 0 540 420">
  <circle cx="138" cy="210" r="136" fill="#fff"/>
  <circle cx="138" cy="210" r="124" fill="var(--grey-ring)"/>
  <circle cx="138" cy="210" r="88" fill="#fff"/>
  <circle cx="138" cy="210" r="72" fill="#eceef1"/>
  <circle role="img" aria-label="Photo of a man holding a laptop and pointing" cx="330" cy="198" r="198" fill="var(--red)"/>
  <path d="M138 190V230M118 210H158" stroke="var(--navy)" stroke-width="2.5"/>
</svg>

<section class="contact-panel abs">
  <h2 class="heading abs" style="left:0;width:813px;top:50px;text-align:center;font-size:44px">CONTACT US</h2>
  <div class="abs" style="left:0;width:813px;top:106px;text-align:center;font-size:15px;color:var(--navy)">Contact Us, We Will Be Happy To Assist You</div>
  <div class="field abs" style="left:39px;top:148px;width:311px;height:47px">Name *</div>
  <div class="field abs" style="left:39px;top:203px;width:311px;height:47px">Email *</div>
  <div class="field abs" style="left:39px;top:257px;width:311px;height:47px">Phone *</div>
  <div class="field abs" style="left:359px;top:148px;width:416px;height:156px">Message *</div>
  <div class="btn abs" style="left:329px;top:316px;width:155px;height:51px;font-size:20px">SUBMIT</div>
</section>

<footer class="abs" style="left:0;top:2150px;width:1200px;height:410px">
  <svg class="abs" style="left:0;top:0" width="1200" height="410" viewBox="0 0 1200 410">
    <path d="M0 6C120 -6 260 20 420 50C620 90 860 60 1050 40C1120 32 1170 42 1200 56V410H0Z" fill="var(--navy)"/>
    <line x1="77" y1="350" x2="1123" y2="350" stroke="#2c394b" stroke-width="1"/>
  </svg>
  <div class="brand abs" style="left:77px;top:135px">
    <div class="brand-name" style="color:#fff">KELDRO<br>SECURITY</div>
    <div class="brand-dot" style="background:#fff"></div>
  </div>
  <div class="social abs" style="left:128px;top:248px;background:var(--red);border-color:var(--red)"></div>
  <div class="social abs" style="left:175px;top:248px"></div>
  <div class="social abs" style="left:222px;top:248px"></div>

  <div class="footer-title abs" style="left:376px;top:148px">SITEMAP</div>
  <div class="footer-list abs" style="left:376px;top:184px">The Start<br>Services<br>Blog<br>Contact</div>

  <div class="footer-title abs" style="left:608px;top:148px">CONTCAT INFO</div>
  <div class="abs" style="left:606px;top:186px;display:flex;flex-direction:column;gap:16px">
    <div class="contact-row"><svg width="18" height="24" viewBox="0 0 18 24"><path d="M9 0C4 0 0 4 0 9C0 15 9 24 9 24S18 15 18 9C18 4 14 0 9 0Z" fill="var(--red)"/><circle cx="9" cy="9" r="3.5" fill="var(--navy)"/></svg><span>Calle Orvena, 14<br>24180 Valtera España</span></div>
    <div class="contact-row"><svg width="18" height="18" viewBox="0 0 18 18"><path d="M4 1L7 5L5 7C6 10 8 12 11 13L13 11L17 14L15 17C8 17 1 10 1 3Z" fill="var(--red)"/></svg><span>+34 900 000 412</span></div>
    <div class="contact-row"><svg width="18" height="14" viewBox="0 0 18 14"><rect width="18" height="14" rx="1" fill="var(--red)"/><path d="M1 1L9 8L17 1" stroke="var(--navy)" stroke-width="1.5" fill="none"/></svg><span>www.keldrosecurity-example.com</span></div>
  </div>

  <div class="footer-title abs" style="left:874px;top:148px">MAP</div>
  <div class="abs" role="img" aria-label="World map" style="left:874px;top:185px;width:250px;height:112px;border-radius:40px;background:linear-gradient(90deg,#9aa1ab,#c6cbd2)"></div>

  <div class="abs" style="left:0;width:1200px;top:370px;text-align:center;font-size:13.5px;color:#b9c0cb">©KELDRO SECURITY - 2018 All Right Reserved.</div>
</footer>

</body>
</html>
```